Whale Watching Voucher(ticket) Layout

Tidalroam.com.au would like a new design for their existing vouchers (tickets) being issued when a customer completes a purchase.
These vouchers are to be issued from within Salesforce CRM using Conga Composer (don't worry about that, we'll handle that) but that does mean that the voucher template needs to be designed and provided in Microsoft Word. The voucher will be sent via an email and we require a HTML email design also.
The following fields need to be included on the email/Voucher:
BOOKING CONFIRMATION NUMBER (e&v)
First Name (e&v)
Tour Name (e&v)
Tour Operator Name (e&v)
Telephone Contact (e&v)
Departure Date (e&v)
Party Name (e&v)
Adults Tickets (v)
Concession Tickets (v)
Child Tickets (v)
Infant Tickets (v)
Pickup Location (v)
Pickup Time (v)
Boarding Place (v)
Boarding Time (v)
Departure Time (v)
Return Time (v)
Terms and conditions (e&v) - this is quite a long description
What to Bring (v) - this is quite a long description
What to do if the Pick-up is more than 10 mins late (v) - this is a long description
What to do if you're late (v) - this is quite a long description
Booking Terms and Conditions
{!Opportunity.Tour_Terms_and_Conditions_PG1__c}
FREECALL 1800 437 962 (Australia)
International +61 7 5926 8174
Skype journeymoss
(e&v indicate fields to be included on the Email and the Voucher)
(v indicate fields to be included on the Voucher only)
Updates
Project Deadline Extended
Reason: I realised the original Deadline didn't take weekends into account so have extended it to the end of this week. The Whale season is well underway so need to have it completed by Friday. Thanks all for your efforts.
I uploaded the current (text based) samples of the email & voucher that we are hoping you are going to be able to redesign for us.
Sorry for lack of feedback, I got caught up on another project. We are reviewing the designs tomorrow and will get back to you all.
Target Market(s)
Mid market Australian and International Tourists
Industry/Entity Type
Purchase
Requirements
Must have
- Consistency with existing Tidalroam.com.au & coralpath.com.au branding.
The Voucher should be designed to be printed out on a single A4 sheet.
Nice to have
- It would be good to have a paragraph/section referencing the coralpath.com.au logo and website on the email (not the voucher).
Any recommendation for additional information/fields that should/could be included not listed above will be gratefully received.
Happy for you to reword the labels to make them more friendly.

```html
<!DOCTYPE html>
<html lang="en">
<head>
<meta charset="utf-8">
<title>E-Ticket Booking Confirmation</title>
<link rel="stylesheet" href="https://fonts.googleapis.com/css2?family=Questrial&family=Arimo:wght@400;700&display=swap">
<style>
:root{
  --backdrop:#2e2520;
  --teal:#13a59a;
  --teal-deep:#0f8f8c;
  --green:#5aab57;
  --green-deep:#2f8a3c;
  --table-head:#3cb3c8;
  --table-line:#4a9db2;
  --ink:#2b2b2b;
  --link-teal:#2b8b9a;
  --call-green:#1e8a3a;
  --orange:#f39323;
  --paper:#ffffff;
  --shadow-grey:#c9c9c9;
}
*{box-sizing:border-box;margin:0;padding:0}
html,body{width:1200px;height:827px;overflow:hidden;background:var(--backdrop)}
body{position:relative;font-family:"Questrial",sans-serif;color:var(--ink)}
.ticket{position:absolute;left:62px;top:37px;width:1075px;height:761px;
  background:linear-gradient(90deg,var(--teal) 0%,var(--teal-deep) 50%,var(--green) 50%,var(--green-deep) 100%)}
.ticket-tag{position:absolute;left:0;top:37px;height:20px;width:96px;background:var(--orange);
  color:#fff;font-family:"Arimo",sans-serif;font-weight:700;font-size:13px;line-height:20px;padding-left:14px;
  clip-path:polygon(0 0,88% 0,100% 50%,88% 100%,0 100%)}
.letter{position:absolute;left:62px;top:52px;width:1056px;height:493px;background:var(--paper);font-size:15px;line-height:18px}
.confirmation{position:absolute;left:46px;top:21px;font-size:15px;white-space:nowrap}
.confirmation .colon{position:absolute;left:324px;top:-4px}
.confirmation .code{position:absolute;left:358px;top:0;font-family:"Arimo",sans-serif;font-size:13px}
.greeting{position:absolute;left:42px;top:51px;width:1010px;white-space:nowrap}
.bookings{position:absolute;left:53px;top:126px;width:967px;border-collapse:collapse;font-size:15px;box-shadow:0 0 4px rgba(0,0,0,.25)}
.bookings th{background:var(--table-head);color:#fff;font-weight:400;height:27px;border:2px solid var(--table-line)}
.bookings td{height:27px;border:2px solid var(--table-line);padding:0 8px}
.bookings .col-tour{width:485px}
.bookings .col-pax{width:248px;text-align:center}
.bookings .col-price{padding-left:88px}
.trip-details{position:absolute;left:42px;top:310px;width:989px;text-align:justify;font-size:15px;line-height:18px}
.trip-note{position:absolute;left:42px;top:415px;width:989px;font-size:15px}
.signoff{position:absolute;left:42px;top:446px}
.photos{position:absolute;left:62px;top:545px;width:1075px;height:133px;display:flex}
.photo{flex:1}
.photo-cruise{background:linear-gradient(180deg,#8fc3e3 0%,#e8eef2 55%,#3d7fb1 100%)}
.photo-lake{background:linear-gradient(180deg,#5e8f4a 0%,#57c6d9 30%,#a5e4e3 100%)}
.photo-rainforest{background:linear-gradient(180deg,#2c6b3a 0%,#4f9a4b 50%,#b2b265 100%)}
.photo-creek{background:linear-gradient(180deg,#6b9a4a 0%,#a8d9d2 55%,#6f8f55 100%)}
.footer{position:absolute;left:62px;top:678px;width:1075px;height:74px;background:var(--paper);font-family:"Arimo",sans-serif;font-weight:700}
.sites{position:absolute;left:26px;top:11px;color:var(--link-teal);font-size:15.5px;line-height:18px}
.brand{position:absolute;top:24px;display:flex;align-items:center;gap:8px;font-family:"Questrial",sans-serif;font-size:17px}
.brand .mark{width:46px;height:46px;border-radius:50%}
.brand-tidal{left:282px;color:var(--teal-deep)}
.brand-tidal .mark{background:var(--teal-deep)}
.brand-coral{left:482px;color:var(--green)}
.brand-coral .mark{background:var(--green)}
.contact{position:absolute;right:56px;top:7px;text-align:right;color:var(--call-green);font-size:14.5px;line-height:18px}
.page-curl{position:absolute;left:80px;top:752px;width:1040px;height:22px}
</style>
</head>
<body>
<div class="ticket"></div>
<div class="ticket-tag">e-ticket</div>

<main class="letter">
  <div class="confirmation">BOOKING CONFIRMATION NUMBER <span class="colon">:</span><span class="code">-Af7862</span></div>
  <div class="greeting">
    <p>Hi Liam and Nora</p>
    <p>Please find below your e-Ticket confirmation and attached vouchers for your booking. Should any of the below details be incorect<br>please let us know ASAP so that they can be amended!</p>
  </div>
  <table class="bookings">
    <thead><tr><th class="col-tour">Tour</th><th class="col-pax">Total passangers</th><th>Total Price</th></tr></thead>
    <tbody>
      <tr><td class="col-tour">1. Day Island Experience Trekker ex. Heervey Bay</td><td class="col-pax">4</td><td class="col-price">980.00</td></tr>
      <tr><td class="col-tour">2. Day/1 Night Island Explorer Tour ex. Hervey Bay</td><td class="col-pax">4</td><td class="col-price">474</td></tr>
      <tr><td class="col-tour">Solara 3/4 Day Whale Watch</td><td class="col-pax">3</td><td class="col-price">474</td></tr>
      <tr><td class="col-tour"></td><td class="col-pax"></td><td class="col-price">980.00</td></tr>
      <tr><td class="col-tour"></td><td class="col-pax"></td><td class="col-price">980.00</td></tr>
    </tbody>
  </table>
  <p class="trip-details">Departure date: Saturday 14 September. Party name: Liam Baker. Tickets: 2 Adults, 1 Concession, 1 Child, 0 Infants. Pick-up location: Bayside Lodge, Hervey Bay at 7:15am. Boarding place: Urangan Marina, boarding time 7:45am. Departure time 8:00am, return time 1:30pm. Tour operator: Solara Cruises, telephone 07 4125 3906. What to bring: hat, sunscreen, warm jacket, camera and binoculars. If your pick-up is more than 10 minutes late, or if you are running late yourself, please call 1800 437 962 straight away so we can hold your seats.</p>
  <p class="trip-note">Booking terms and conditions apply, please read them on your attached voucher before you travel.</p>
  <div class="signoff"><p>Cheers!</p><p>Liam</p></div>
</main>

<section class="photos">
  <div class="photo photo-cruise" role="img" aria-label="Whale watching cruise boat on the bay"></div>
  <div class="photo photo-lake" role="img" aria-label="Couple splashing in a clear freshwater lake"></div>
  <div class="photo photo-rainforest" role="img" aria-label="Sandy track through lush rainforest"></div>
  <div class="photo photo-creek" role="img" aria-label="Couple wading along a shallow creek"></div>
</section>

<footer class="footer">
  <div class="sites">www.coralpath.com.au<br>tidalroam.com.au</div>
  <div class="brand brand-tidal"><span class="mark"></span>Tidalroam</div>
  <div class="brand brand-coral"><span class="mark"></span>Coralpath</div>
  <div class="contact">FREECALL 1800 437 962 (Australia)<br>International +61 7 5926 8174<br>Skype journeymoss</div>
</footer>

<svg class="page-curl" viewBox="0 0 1040 22" preserveAspectRatio="none" aria-hidden="true">
  <path d="M0 0 H1040 L1032 18 Q520 8 8 18 Z" fill="var(--shadow-grey)"/>
</svg>
</body>
</html>
```